Net Clarity Partners Needs a New Business Card Design

Attached is my new logo that ArtFlockly created and picture of me for the back of the business card. Also attached is the information to include on the business card (on my existing business card design - NCP1 file attached).

The designer also provided a treatment of my logo that I really like if you can use it somehow. Also attached - file name "Preferred Version of New Logo."

Marla Quinteros

Net Clarity Partners
4817 Brindle Ave., #315
Houston, TX 77056

Tel: (832) 555-0147
www.netclaritypartners.example
marla@netclaritypartners.example

Thank you.

Target Market(s)

attorneys and law firms

Industry/Entity Type

Legal

Contact Information for Business Card

Proved in the Project Description

Font styles to use
Other font styles liked:
• I am open on font - no script though.

Colors
2d73b3
33a6d7

Requirements
Must have
• my logo
• company name & contact info
• my picture on the back
• colors that coordinate with the logo
Nice to have
• love to use the treated version of the logo if possible

```html
<!DOCTYPE html>
<html lang="en">
<head>
<meta charset="utf-8">
<title>Net Clarity Partners – Business Card</title>
<link href="https://fonts.googleapis.com/css2?family=Lato:wght@400;700;900&display=swap" rel="stylesheet">
<style>
  :root {
    --stage: #2b2b2c;
    --card-dark: #3b3939;
    --card-dark-edge: #2f2d2d;
    --card-light: #f7f7f7;
    --brand-blue: #33a6d7;
    --brand-deep: #2d73b3;
    --band-blue: #2a93c6;
    --ink: #2f2f2f;
    --muted: #b9b9b9;
    --white: #ffffff;
  }
  * { box-sizing: border-box; margin: 0; padding: 0; }
  html, body { width: 1200px; height: 873px; overflow: hidden; }
  body {
    background: var(--stage);
    font-family: "Lato", Arial, sans-serif;
    position: relative;
  }
  .card {
    position: absolute;
    width: 560px;
    height: 320px;
    border-radius: 16px;
    overflow: hidden;
    box-shadow: 0 14px 30px rgba(0,0,0,0.45);
  }

  /* Front of card */
  .card-front {
    left: 60px;
    top: 90px;
    background: linear-gradient(135deg, var(--card-dark) 0%, var(--card-dark-edge) 100%);
  }
  .portrait {
    position: absolute;
    right: 0;
    top: 0;
    width: 270px;
    height: 320px;
    background: linear-gradient(160deg, #5a5250 0%, #b39a7e 38%, #3b3ec0 75%, #2b2fa0 100%);
  }
  .holder {
    position: absolute;
    left: 40px;
    top: 120px;
  }
  .holder-name {
    color: var(--brand-blue);
    font-weight: 900;
    font-size: 28px;
    letter-spacing: 0.3px;
    white-space: nowrap;
  }
  .holder-title {
    color: var(--muted);
    font-weight: 700;
    font-size: 12px;
    letter-spacing: 3px;
    margin-top: 4px;
    padding-left: 60px;
  }
  .front-brand {
    position: absolute;
    left: 40px;
    bottom: 52px;
    display: flex;
    align-items: center;
    gap: 8px;
  }
  .brand-mark {
    width: 12px;
    height: 12px;
    background: var(--brand-blue);
    flex: none;
  }
  .brand-name {
    color: var(--brand-blue);
    font-weight: 900;
    font-size: 18px;
    text-transform: uppercase;
    letter-spacing: 0.4px;
    white-space: nowrap;
  }

  /* Back of card */
  .card-back {
    left: 580px;
    top: 460px;
    background: linear-gradient(180deg, var(--white) 0%, var(--card-light) 100%);
  }
  .back-brand {
    position: absolute;
    left: 26px;
    top: 122px;
    display: flex;
    align-items: center;
    gap: 7px;
  }
  .back-brand .brand-name { font-size: 15px; }
  .back-brand .brand-mark { width: 10px; height: 10px; }
  .divider {
    position: absolute;
    left: 254px;
    top: 70px;
    width: 2px;
    height: 140px;
    background: linear-gradient(180deg, rgba(51,166,215,0) 0%, var(--brand-blue) 40%, rgba(51,166,215,0) 100%);
  }
  .contact-list {
    position: absolute;
    left: 268px;
    top: 92px;
    list-style: none;
  }
  .contact-list li {
    display: flex;
    align-items: center;
    gap: 7px;
    color: var(--ink);
    font-size: 12px;
    font-weight: 400;
    height: 26px;
    white-space: nowrap;
  }
  .contact-list svg { width: 14px; height: 14px; flex: none; }
  .web-band {
    position: absolute;
    left: 0;
    right: 0;
    bottom: 0;
    height: 62px;
    background: var(--band-blue);
    color: var(--white);
    display: flex;
    align-items: center;
    justify-content: center;
    font-weight: 700;
    font-size: 15px;
    letter-spacing: 3px;
  }
</style>
</head>
<body>

  <section class="card card-front">
    <div class="portrait" role="img" aria-label="Portrait photograph of Marla Quinteros"></div>
    <div class="holder">
      <div class="holder-name">Marla Quinteros</div>
      <div class="holder-title">FOUNDER</div>
    </div>
    <div class="front-brand">
      <span class="brand-mark"></span>
      <span class="brand-name">Net Clarity Partners</span>
    </div>
  </section>

  <section class="card card-back">
    <div class="back-brand">
      <span class="brand-mark"></span>
      <span class="brand-name">Net Clarity Partners</span>
    </div>
    <div class="divider"></div>
    <ul class="contact-list">
      <li>
        <svg viewBox="0 0 24 24" aria-hidden="true"><path fill="#2a93c6" d="M6.6 10.8a15.1 15.1 0 0 0 6.6 6.6l2.2-2.2a1 1 0 0 1 1-.25 11.4 11.4 0 0 0 3.6.57 1 1 0 0 1 1 1V20a1 1 0 0 1-1 1A17 17 0 0 1 3 4a1 1 0 0 1 1-1h3.5a1 1 0 0 1 1 1c0 1.25.2 2.45.57 3.57a1 1 0 0 1-.25 1z"/></svg>
        (832) 555-0147
      </li>
      <li>
        <svg viewBox="0 0 24 24" aria-hidden="true"><rect x="2" y="5" width="20" height="14" rx="1.5" fill="#2a93c6"/><path d="M3 6.5l9 6.5 9-6.5" fill="none" stroke="#fff" stroke-width="1.6"/></svg>
        marla@netclaritypartners.example
      </li>
      <li>
        <svg viewBox="0 0 24 24" aria-hidden="true"><path fill="#2a93c6" d="M12 2a7 7 0 0 0-7 7c0 5.2 7 13 7 13s7-7.8 7-13a7 7 0 0 0-7-7zm0 9.5A2.5 2.5 0 1 1 12 6.5a2.5 2.5 0 0 1 0 5z"/></svg>
        4817 Brindle Ave, #315, Houston, TX 77056
      </li>
    </ul>
    <div class="web-band">www.netclaritypartners.example</div>
  </section>

</body>
</html>
```